Poster design for a vet clinic

Running a campaign called 'Tail teller', which is where people get a $30 voucher for themselves and their friend if they refer somebody to our vet clinic.

Text something like:
We love Tail Tellers!
Refer a fur friend to our friendly team and both your fur child and their fur child will receive a $30 voucher to use in clinic! *
* Limited to one pet per fur parent and the referred fur parent must be new to our clinic. Unlimited vouchers for number of referrals!

I want it to be cute but professional. You can see the design styles at mossbury-vet.com.au/kelvale and see the logo there too.
I am thinking of having a dog whispering to a cat or something like that as the main image.
I would like both the photoshop file and the pdf please. Would be for an A2 poster.

```html
<!DOCTYPE html>
<html lang="en">
<head>
<meta charset="utf-8">
<title>Mossbury Veterinary Clinic – We Love Tail Tellers</title>
<link rel="stylesheet" href="https://fonts.googleapis.com/css2?family=Lilita+One&family=Fredoka:wght@400;600&display=swap">
<style>
  :root {
    --brown: #6c4f45;
    --orange: #f7941d;
    --white: #ffffff;
    --tan: #c9a08f;
  }
  * { margin: 0; padding: 0; box-sizing: border-box; }
  html, body { width: 848px; height: 1200px; overflow: hidden; background: var(--brown); }
  .poster { position: relative; width: 848px; height: 1200px; background: var(--brown); overflow: hidden; }
  .bubble { position: absolute; inset: 0; }
  .logo-tab {
    position: absolute; left: 224px; top: 0; width: 408px; height: 236px;
    background: var(--brown); border-radius: 0 0 40px 40px;
    display: flex; flex-direction: column; align-items: center; padding-top: 54px;
    font-family: "Fredoka", sans-serif;
  }
  .logo-name { display: flex; align-items: center; gap: 12px; color: var(--white); font-weight: 600; font-size: 62px; line-height: 1; }
  .logo-dot { width: 22px; height: 22px; border-radius: 50%; background: var(--orange); }
  .logo-sub { color: var(--white); font-weight: 600; font-size: 16px; letter-spacing: 2px; margin-top: 14px; }
  .logo-rule { width: 270px; height: 2px; background: var(--orange); margin-top: 6px; }
  .logo-place { color: var(--orange); font-weight: 400; font-size: 30px; margin-top: 6px; }
  .price-badge { position: absolute; left: 656px; top: 56px; width: 128px; height: 128px; }
  .headline {
    position: absolute; left: 0; width: 848px; top: 252px; text-align: center;
    font-family: "Lilita One", sans-serif; color: var(--orange);
    font-size: 86px; line-height: 88px; text-transform: uppercase;
  }
  .offer {
    position: absolute; left: 0; width: 848px; top: 432px; text-align: center;
    font-family: "Lilita One", sans-serif; color: var(--brown);
    font-size: 36px; line-height: 37.5px; text-transform: uppercase;
  }
  .terms {
    position: absolute; left: 0; width: 848px; top: 652px; text-align: center;
    font-family: "Lilita One", sans-serif; color: var(--brown);
    font-size: 20px; line-height: 24px; text-transform: uppercase;
  }
  .mascots {
    position: absolute; left: 0; top: 790px; width: 848px; height: 410px;
    background: linear-gradient(180deg, #f7941d 0%, #fbc98a 45%, #6c4f45 100%);
  }
</style>
</head>
<body>
<main class="poster">
  <svg class="bubble" width="848" height="1200" viewBox="0 0 848 1200" aria-hidden="true">
    <path fill="#ffffff" d="M80 22 H776 Q812 22 812 60 L800 880 Q798 930 750 930 H460 L300 1000 L340 930 H90 Q44 930 46 880 L36 70 Q36 22 80 22 Z"/>
  </svg>

  <header class="logo-tab">
    <div class="logo-name"><span class="logo-dot"></span>Mossbury</div>
    <div class="logo-sub">VETERINARY CLINIC</div>
    <div class="logo-rule"></div>
    <div class="logo-place">KELVALE</div>
  </header>

  <svg class="price-badge" viewBox="0 0 128 128" aria-label="$30">
    <circle cx="64" cy="64" r="56" fill="#6c4f45" stroke="#6c4f45" stroke-width="10" stroke-dasharray="4 6"/>
    <text x="64" y="76" text-anchor="middle" transform="rotate(18 64 64)" font-family="Lilita One, sans-serif" font-size="40" fill="#c9a08f">$30</text>
  </svg>

  <h1 class="headline">We Love<br>Tail Tellers!</h1>

  <p class="offer">Refer a fur friend<br>to our friendly team and both<br>your fur child and their fur child<br>will receive<br>a $30 voucher to use in clinic!*</p>

  <p class="terms">* Limited to one pet per fur parent<br>and the referred fur parent must be new to our clinic.<br>Unlimited vouchers for number of referrals!</p>

  <div class="mascots" role="img" aria-label="Cartoon dog whispering to a cartoon cat with heart eyes"></div>
</main>
</body>
</html>
```